Vendro Sahel - Website Design Brief

Web Design Brief

VENDRO SAHEL
WEBSITE DESIGN BRIEF

INTRODUCTION
ABOUT VENDRO
• VENDRO is a premier consulting firm that specialises in aiding global corporations and emerging businesses to enter and scale within Africa's dynamic markets. Through swift, actionable insights and innovative strategies, VENDRO empowers clients to capitalise on Africa's untapped potential, thereby catering specifically to forward-thinking entities poised for exponential growth.

TASK DESCRIPTION
• Develop a 5-page website for VENDRO.
• The primary goal is to present a clear and concise picture of our consulting firm, its Africa-centric experience, and its offerings to multinational clients looking for a professional partner to penetrate African markets or reclaim lost market share.

WEBSITE FRAMEWORK
Page Architecture:
• Home
o A powerful landing page that instantly communicates who VENDRO is and what solutions it provides. Incorporate impactful visuals and calls-to-action.
• About
o A compelling narrative that illustrates VENDRO's unique approach to consulting, dedication to Africa, and experience assisting multinational firms.
• Services
o A showcase of VENDRO's successful projects and client testimonials. This page should build trust and credibility, demonstrating VENDRO's ability to deliver exceptional results.
• Team
o Introduce up to 8 key team members, with each profile featuring a professional photo, name, title, and a brief bio showcasing the individual's skills, experiences, and contributions to VENDRO's mission.
• Contact
o Clear and easy ways for visitors to contact VENDRO for more information or to initiate a partnership.
• Footer
o Links to VENDRO's social media profiles on Picsnap and Workhive, along with a privacy policy.
o Social links
o Picsnap: https://www.instagram.com/vendrosahel/
o Workhive: https://www.linkedin.com/company/vendrosahel/
o Privacy Policy
o Insert placeholder "lorem ipsum" text.
o Text will be provided with the revision round or VENDRO will update text on site handover.

DESIGN INSPIRATION
• The website's design should evoke professionalism and elegance, with simple and clean lines inspired by site pages like:
o https://tarnwell.example/
o https://tarnwell.example/services/
o One aspect we particularly appreciate is how visitors can easily navigate by scrolling down to find what they're looking for and see everything they need to in an intuitive way on the home page
o What we don’t like about this site is how they navigate from the home page to other random pages – we like about to take you to the about page, and so on.

Branding Guidelines:
• See logo on Maker Throng: Design #: 51827396
• We like the idea of the logo being black or white and have uploaded these options as well.
• Monochrome themes, with spots or splash of colour to highlight something is a style we appreciate.

Website Objectives and Goals:
• Our website's primary goal is to create a strong online presence, acting as a hub for potential clients to discover our credibility, reliability, and our ability to deliver exceptional results. It's essential that our website portrays professionalism, instils trustworthiness, and showcases our sincere dedication to Africa.

Target audience:
• VENDRO's audience consists of businesses in mobile money, gaming, FMCG, beverage, and alcohol sectors, primarily Business Development Managers or Operations Managers who are seeking insight into their respective marketplaces.

Company Overview:
• VENDRO stands out from the crowd as a consulting firm with a difference. Our dynamic team is fully dedicated to one mission: brand development within Africa.
• Unlike other companies that focus solely on online connectivity, we recognize the tremendous value in embracing the vibrant street culture that makes Africa so unique. Community engagement, empowerment, and expansion are at the forefront of everything we do.
• we recognize that unlocking business growth starts with a deep understanding of consumer behavior. It is this understanding that bridges the gap between companies and the communities that drive the cash economy. Our purpose is to reconnect businesses with the vibrant pulse of these essential local markets, injecting fresh vitality into their brands and propelling them towards resounding success in Africa.

Development to include:
• Basic SEO Setup:
o The website should be optimized for search engines, incorporating keywords, meta tags, and alt tags for images.
• Searchly Metrics Setup.
o To track website traffic and user behaviour for ongoing optimization.
• Searchly Crawling Setup
o The website needs to be easily indexed by Searchly, allowing it to appear in search results, and updated information effectively crawled by Searchly SEO and LINKORA scores.

PAGE CONTENT:
Home Page
• Background
o Option #1
o 4K video on home page, running on loop
o Bold Statement Text over Video
o Option #2
o Still Image
o Animated text making bold statement (e.g. our motto)

• Sections
o Contrast colour blocks or a way of making it clear that the next topic is a new topic.
o 5 sections
1. Home Main - Video + bold statement text
2. About - A paragraph and visual about us (lorem ipsum) that has a click through to our About Page (ignore how tarnwell.example navigate, we think this is too complicated for our needs)
3. Services – communicated in some simple and powerful ways (we leave this open to you) – but keeping in mind it needs to be concise and professional.
4. Other - Something about our process that makes us unique (lorem ipsum text) and a placeholder image/animation.
5. Contact – a call-to-action button that takes you to our contact, but showcases a mobile number and email address.
6. Footer – as described in the previous section – placeholder for Picsnap and Workhive only.

About Page
• Don’t reference tarnwell.example for this page.
• Main Section
o Bold statements and images
• History Section
o A story about us and our past
• Final Section
o Some of our comments and final thoughts

Services Page
• How https://tarnwell.example/services/ is laid out is great – we prefer a light theme.
• 6 - 8 x icons with headings and a brief description text box, and a read more drop down – all as placeholders to be edited later.
• For ease of direction for this page, look to the link shared above.

Team
• Add Placeholders for up to 8 team members (we only have 4 now):
o Image placeholder
o Name placeholder
o Title placeholder
o Short Bio (lorem ipsum)

Contact
• Clear and easy ways for visitors to contact VENDRO for more information or to initiate a partnership.

• Insert placeholder "lorem ipsum" text, we will provide the text with our revision round.
o Ideally an easy form process that gives the user some options or dropdowns to complete before submission – up to 3 would be sufficient.
o Require their name and contact details.

NOTE: Images to follow:

Target Market(s)

VENDRO's audience consists of businesses in mobile money, gaming, FMCG, beverage, and alcohol sectors, primarily Business Development Managers or Operations Managers who are seeking insight into their respective marketplaces.

Industry/Entity Type

VENDRO is a premier consulting firm that specialises in aiding global corporations and emerging businesses to enter and scale within Africa's dynamic markets

Coding

Coded - Design and coding required

Number of Pages Required

5+ page

Font styles to use
Sans Serif
Other font styles liked:
• Poppins Font Family

Colors

Designer to choose colors to be used in the design.

Requirements
Must have
• The primary goal is to present a clear and concise picture of our consulting firm, and it's specialisation in Africa - smooth and crisp UI with animations or transitions that imply we know our way around tecchnology is always helpful - but a Clean and responsive UI is most important.
Nice to have
• Reactive and animated transitions through sections or pages - not overdone - adds a professional feel to the site
Should not have
• We don't want too many colours, and we don't want it too dark - we want a monochrome theme, with accents of colour when relevant

```html
<!DOCTYPE html>
<html lang="en">
<head>
<meta charset="utf-8">
<title>Vendro Sahel — Growth and Transformation Consulting</title>
<link href="https://fonts.googleapis.com/css2?family=Comfortaa:wght@300;400;500&family=Poppins:wght@300;400;500;600&display=swap" rel="stylesheet">
<style>
:root{
  --navy:#04101c;
  --navy-2:#0b2a44;
  --blue:#0a72c2;
  --blue-deep:#0461ad;
  --sky:#1f9bf0;
  --ink:#1d1f24;
  --muted:#5c6168;
  --light:#ececec;
  --white:#ffffff;
  --line:#d9dde2;
}
*{margin:0;padding:0;box-sizing:border-box}
html,body{width:1200px;height:4471px;overflow:hidden}
body{position:relative;font-family:"Poppins",sans-serif;color:var(--ink);background:var(--white)}
.abs{position:absolute}
.display{font-family:"Comfortaa",sans-serif;font-weight:400}

/* hero */
.hero{left:0;top:0;width:1200px;height:677px;background:linear-gradient(100deg,var(--navy-2) 0%,var(--navy) 45%,#020509 100%)}
.brand{display:flex;align-items:center;gap:10px;color:var(--white);font-family:"Comfortaa",sans-serif;font-size:34px;letter-spacing:1px}
.brand-mark{width:34px;height:34px;border:3px solid var(--white)}
.nav{right:88px;top:44px;display:flex;gap:24px;font-size:12.5px;font-weight:500;color:var(--white)}
.nav .active{color:var(--sky)}
.hero-title{left:88px;top:150px;width:480px;color:var(--white);font-size:60px;line-height:63px;font-weight:300}
.hero-sub{left:88px;top:486px;color:#dfe6ee;font-size:14px;font-family:"Comfortaa",sans-serif}
.btn{display:flex;align-items:center;justify-content:center;font-size:11px;font-weight:600;letter-spacing:.4px;text-transform:uppercase}
.btn-solid{background:var(--blue);color:var(--white)}
.btn-ghost{border:2px solid var(--white);color:var(--white)}
.hero-media{left:610px;top:115px;width:500px;height:622px;background:linear-gradient(160deg,#3e6f94 0%,#8f8a6f 35%,#c7a84a 55%,#4f8f78 80%,#2f5c6e 100%);box-shadow:0 40px 50px -20px rgba(0,0,0,.35)}
.play{left:202px;top:264px;width:94px;height:94px;border-radius:50%;background:var(--white)}

/* about */
.section-title{left:0;width:1200px;text-align:center;font-size:38px}
.rule{width:56px;height:2px;left:572px;background:#bfc4ca}
.about-text{left:270px;top:940px;width:660px;text-align:center;font-size:14.5px;line-height:25px;color:#3c4046}
.blue-band{left:0;top:1636px;width:1200px;height:726px;background:linear-gradient(90deg,var(--blue) 0%,var(--blue-deep) 100%)}
.about-photo{left:88px;top:1138px;width:1112px;height:596px;background:linear-gradient(120deg,#9c7f52 0%,#c9a248 30%,#8b8e86 50%,#5e8e6c 75%,#2f5a3a 100%)}

/* services */
.services-title{color:var(--white);top:1815px}
.services-sub{left:300px;top:1900px;width:600px;text-align:center;color:#e6f1fb;font-size:14.5px;line-height:25px}
.service{width:220px;color:var(--white)}
.service svg{display:block;margin-bottom:26px}
.service h3{font-family:"Comfortaa",sans-serif;font-weight:500;font-size:19px;line-height:22px;margin-bottom:16px}
.service p{font-size:12.5px;line-height:20px;color:#e3eefa;margin-bottom:14px}
.dot{width:26px;height:26px;border-radius:50%;background:rgba(255,255,255,.28)}
.btn-outline-light{left:549px;top:2256px;width:101px;height:39px;border:2px solid var(--white);color:var(--white)}

/* process */
.step-num{font-family:"Comfortaa",sans-serif;font-size:27px;color:#c8ccd1}
.step h4{font-family:"Comfortaa",sans-serif;font-weight:500;font-size:19px;line-height:22px;color:var(--ink)}
.step p{font-size:11.5px;line-height:18px;color:var(--muted);margin-top:14px;width:225px}
.step-head{display:flex;gap:12px;align-items:flex-start}

/* testimonials */
.testi-band{left:0;top:2979px;width:1200px;height:498px;background:var(--light)}
.card{top:3187px;width:329px;height:200px;background:var(--white);border-radius:8px;box-shadow:0 12px 30px rgba(0,0,0,.08)}
.card .avatar{left:36px;top:-36px;width:72px;height:72px;border-radius:50%}
.card .quote{left:26px;top:66px;width:280px;font-size:12.5px;line-height:22px;color:#44484e}
.card .name{left:24px;top:160px;font-family:"Comfortaa",sans-serif;font-size:13px;color:var(--ink)}
.card .stars{right:26px;top:158px;color:#f5b301;font-size:13px;letter-spacing:1px}
.card .qmark{right:80px;top:14px;font-family:"Comfortaa",sans-serif;font-size:80px;color:#e5e7ea;line-height:80px}

/* cta */
.cta-title{left:88px;top:3650px;font-size:44px}
.cta-sub{left:88px;top:3730px;font-family:"Comfortaa",sans-serif;font-size:17px;line-height:23px;color:#4b5056}
.cta-art{left:573px;top:3509px;width:539px;height:451px;background:radial-gradient(ellipse at 50% 50%,#cfeefc 0%,#e9f5fc 45%,#ffffff 75%)}

/* footer */
.footer{left:0;top:3986px;width:1200px;height:485px;background:linear-gradient(180deg,#0e2236 0%,var(--navy) 45%,#02060b 100%)}
.social{display:flex;align-items:center;justify-content:center;height:44px;padding:0 10px;background:rgba(255,255,255,.1);color:var(--white);font-size:11px}
.foot-h{font-family:"Comfortaa",sans-serif;font-size:27px;color:var(--white)}
.quick{left:432px;top:4122px;width:145px}
.quick a{display:block;color:#d0d7df;font-size:13px;text-decoration:none;padding:10px 0 11px;border-bottom:1px solid rgba(255,255,255,.12)}
.foot-text{font-size:12.5px;line-height:18px;color:#cdd4dc;width:430px}
.to-top{left:1138px;top:4389px;width:37px;height:37px;background:var(--blue)}
.foot-rule{left:88px;top:4412px;width:1024px;height:1px;background:rgba(255,255,255,.15)}
.copyright{left:0;top:4432px;width:1200px;text-align:center;color:#d6dce2;font-size:13px}
</style>
</head>
<body>

<!-- Hero -->
<section class="abs hero">
  <div class="abs brand" style="left:88px;top:32px"><span class="brand-mark"></span>VENDRO</div>
  <nav class="abs nav"><span class="active">HOME</span><span>ABOUT</span><span>SERVICES</span><span>TEAM</span><span>CONTACT</span></nav>
  <h1 class="abs hero-title display">We Are a Growth and Transformation Consulting Firm.</h1>
  <p class="abs hero-sub">We are a growth and transformation consulting firm.</p>
  <a class="abs btn btn-solid" style="left:88px;top:532px;width:132px;height:38px">About Vendro</a>
  <a class="abs btn btn-ghost" style="left:230px;top:532px;width:131px;height:38px">Our Service</a>
</section>
<div class="abs hero-media" role="img" aria-label="Aerial video of a busy African market street with minibuses and a footbridge">
  <div class="abs play">
    <svg width="94" height="94" viewBox="0 0 94 94"><path d="M42 40 L54 47 L42 54 Z" fill="#111"/></svg>
  </div>
</div>

<!-- About -->
<h2 class="abs section-title display" style="top:860px">Welcome To About Vendro</h2>
<div class="abs rule" style="top:918px"></div>
<p class="abs about-text">VENDRO is a premier consulting firm that specialises in aiding global corporations and emerging businesses to enter and scale within Africa's dynamic markets. Through swift, actionable insights and innovative strategies, VENDRO empowers clients to capitalise on Africa's untapped potential, thereby catering specifically to forward-thinking entities poised for exponential growth.</p>

<div class="abs blue-band"></div>
<div class="abs about-photo" role="img" aria-label="Aerial photo of a crowded market road with buses and a green pedestrian bridge"></div>

<!-- Services -->
<h2 class="abs section-title display services-title">Vendro Services</h2>
<div class="abs rule" style="top:1876px;background:#fff"></div>
<p class="abs services-sub">VENDRO clients achieve exceptional revenue gains, thanks to rich customer insights and a human-centered approach to growth.</p>

<div class="abs service" style="left:158px;top:1985px">
  <svg width="66" height="66" viewBox="0 0 66 66" fill="none" stroke="#fff" stroke-width="2"><circle cx="42" cy="18" r="12"/><circle cx="42" cy="15" r="4"/><path d="M6 30l8 8M14 30l-8 8M6 52l8 8M14 52l-8 8M18 48c10 0 10-12 20-16"/></svg>
  <h3>Identify Growth Pathways</h3>
  <p>VENDRO clients achieve exceptional revenue.</p>
  <div class="dot"></div>
</div>
<div class="abs service" style="left:410px;top:1985px">
  <svg width="66" height="66" viewBox="0 0 66 66" fill="none" stroke="#fff" stroke-width="2"><circle cx="33" cy="12" r="5"/><circle cx="33" cy="33" r="6"/><circle cx="10" cy="24" r="4"/><circle cx="56" cy="24" r="4"/><circle cx="10" cy="48" r="4"/><circle cx="56" cy="48" r="4"/><circle cx="33" cy="56" r="5"/><path d="M14 24h13M39 24h13M14 48h13M39 48h13M33 17v10M33 39v12"/></svg>
  <h3>Drive Customer Demand</h3>
  <p>VENDRO clients achieve exceptional revenue.</p>
  <div class="dot"></div>
</div>
<div class="abs service" style="left:660px;top:1985px">
  <svg width="66" height="66" viewBox="0 0 66 66" fill="none" stroke="#fff" stroke-width="2"><rect x="2" y="4" width="62" height="56"/><path d="M2 14h62M16 36c10-12 24-12 34 0c-10 12-24 12-34 0z"/><circle cx="33" cy="36" r="5"/></svg>
  <h3>Reimagine Brands</h3>
  <p>VENDRO clients achieve exceptional revenue.</p>
  <div class="dot"></div>
</div>
<div class="abs service" style="left:910px;top:1985px">
  <svg width="66" height="66" viewBox="0 0 66 66" fill="none" stroke="#fff" stroke-width="2"><circle cx="33" cy="8" r="5"/><path d="M26 20c0-6 14-6 14 0"/><circle cx="10" cy="32" r="5"/><path d="M3 44c0-6 14-6 14 0"/><circle cx="56" cy="32" r="5"/><path d="M49 44c0-6 14-6 14 0"/><circle cx="33" cy="52" r="5"/><path d="M26 64c0-6 14-6 14 0M18 14l-4 6M48 14l4 6"/></svg>
  <h3>Empower Employees</h3>
  <p>VENDRO clients achieve exceptional revenue.</p>
  <div class="dot"></div>
</div>
<a class="abs btn btn-outline-light">View All</a>

<!-- Process -->
<h2 class="abs section-title display" style="top:2440px">Vendro Process</h2>
<div class="abs rule" style="top:2501px"></div>

<svg class="abs" style="left:0;top:2520px" width="1200" height="260" viewBox="0 0 1200 260">
  <defs>
    <filter id="soft" x="-50%" y="-50%" width="200%" height="200%"><feDropShadow dx="0" dy="10" stdDeviation="8" flood-color="#0a72c2" flood-opacity=".18"/></filter>
  </defs>
  <g stroke="#e6e8eb" stroke-width="14" stroke-linecap="round">
    <path d="M290 90 L410 150"/><path d="M530 150 L650 90"/><path d="M770 90 L890 150"/>
  </g>
  <g fill="none" stroke="#0a72c2" stroke-width="4" stroke-linecap="round" filter="url(#soft)">
    <path d="M156 40 Q231 100 306 40"/>
    <path d="M397 160 Q472 220 547 160"/>
    <path d="M632 40 Q707 100 782 40"/>
    <path d="M875 160 Q950 220 1025 160"/>
  </g>
  <g fill="none" stroke="#0a72c2" stroke-width="2">
    <rect x="213" y="30" width="36" height="22"/><path d="M209 30 L231 16 L253 30"/><path d="M220 46 l8 4 l10-8"/>
    <rect x="455" y="148" width="36" height="28"/><path d="M461 156h24M461 164h16"/><circle cx="458" cy="176" r="6"/>
    <circle cx="707" cy="16" r="6"/><path d="M693 46 q14-18 28 0"/><circle cx="694" cy="34" r="5"/><circle cx="720" cy="34" r="5"/><path d="M684 52h46"/>
    <circle cx="950" cy="140" r="8"/><circle cx="936" cy="160" r="6"/><circle cx="964" cy="160" r="6"/><path d="M944 146l-4 8M956 146l4 8M942 160h16"/>
  </g>
</svg>

<div class="abs step" style="left:142px;top:2690px">
  <div class="step-head"><span class="step-num">01</span><h4>Acquiring<br>Projects</h4></div>
  <p>VENDRO clients achieve exceptional revenue gains, thanks to rich...</p>
</div>
<div class="abs step" style="left:391px;top:2806px">
  <div class="step-head"><span class="step-num">02</span><h4>Consulting<br>Practices</h4></div>
  <p>VENDRO clients achieve exceptional revenue gains, thanks to rich...</p>
</div>
<div class="abs step" style="left:624px;top:2690px">
  <div class="step-head"><span class="step-num">03</span><h4>Communicating<br>Results</h4></div>
  <p>VENDRO clients achieve exceptional revenue gains, thanks to rich...</p>
</div>
<div class="abs step" style="left:881px;top:2806px">
  <div class="step-head"><span class="step-num">04</span><h4>Coordinating<br>Expectations</h4></div>
  <p>VENDRO clients achieve exceptional revenue gains, thanks to rich...</p>
</div>

<!-- Testimonials -->
<div class="abs testi-band"></div>
<h2 class="abs section-title display" style="top:3060px">What Our Customer Say</h2>
<div class="abs rule" style="top:3120px"></div>

<article class="abs card" style="left:90px">
  <div class="abs avatar" role="img" aria-label="Client portrait" style="background:#d9a23d"></div>
  <span class="abs qmark">&ldquo;</span>
  <p class="abs quote">"Very professional, courteous and fast. Orvane seems to have solved all of our issues that we've been."</p>
  <span class="abs name">Dario Quell</span><span class="abs stars">★★★★★</span>
</article>
<article class="abs card" style="left:436px">
  <div class="abs avatar" role="img" aria-label="Client portrait" style="background:#8f8fd6"></div>
  <span class="abs qmark">&ldquo;</span>
  <p class="abs quote">"Very professional, courteous and fast. Orvane seems to have solved all of our issues that we've been."</p>
  <span class="abs name">Milo Fenwick</span><span class="abs stars">★★★★★</span>
</article>
<article class="abs card" style="left:782px">
  <div class="abs avatar" role="img" aria-label="Client portrait" style="background:#e0563a"></div>
  <span class="abs qmark">&ldquo;</span>
  <p class="abs quote">"Very professional, courteous and fast. Orvane seems to have solved all of our issues that we've been."</p>
  <span class="abs name">Dario Quell</span><span class="abs stars">★★★★★</span>
</article>

<!-- Call to action -->
<h2 class="abs cta-title display">Let’s Grow Together</h2>
<p class="abs cta-sub">Have questions about your next growth move?<br>Tarnwell has answers.</p>
<a class="abs btn btn-solid" style="left:88px;top:3792px;width:132px;height:38px">Contact Us</a>
<div class="abs cta-art" role="img" aria-label="Illustration of floating blue and white isometric cubes"></div>

<!-- Footer -->
<footer class="abs footer">
  <div class="abs brand" style="left:134px;top:170px;font-size:42px"><span class="brand-mark" style="width:42px;height:42px"></span>VENDRO</div>
  <div class="abs" style="left:186px;top:241px;display:flex;gap:8px">
    <a class="social">Workhive</a><a class="social">Picsnap</a>
  </div>
  <h3 class="abs foot-h" style="left:432px;top:92px">Quick Links</h3>
  <h3 class="abs foot-h" style="left:665px;top:92px">Contact Us</h3>
  <p class="abs foot-text" style="left:665px;top:138px">VENDRO is a premier consulting firm that specialises in aiding global corporations and emerging businesses to enter and scale within Africa's dynamic</p>
  <h3 class="abs foot-h" style="left:665px;top:230px">Privacy Policy</h3>
  <p class="abs foot-text" style="left:665px;top:276px">VENDRO is a premier consulting firm that specialises in aiding global corporations and emerging businesses to enter and scale within Africa's dynamic</p>
</footer>
<nav class="abs quick">
  <a>Home</a><a>About</a><a>Services</a><a>Team</a><a style="border-bottom:none">Contact</a>
</nav>
<div class="abs foot-rule"></div>
<div class="abs to-top"><svg width="37" height="37" viewBox="0 0 37 37"><path d="M14 21l4.5-5 4.5 5" fill="none" stroke="#fff" stroke-width="2"/></svg></div>
<p class="abs copyright">© Copyright 2023 Vendro, All Rights Reserved</p>

</body>
</html>
```